Business Card Design/Stationary Design

We would like designers to submit cool, hip business card designs (plus stationary designs) for a new, upstart software development company located in Toronto.
If you have any questions, please email us.
For inspiration on designs:
http://cardmuse.example/cool-business-cards/
http://layoutnotes.example/2008/05/36-cool-business-cards-you-should%E2%80%99ve-seen.html
http://gigharbor.example/general/18-smokin-hot-business-card-designs/

Card info:

Selvakumar (Selv) Nadarasan

Founder and CEO

47 Brindle Court, Suite 311

Toronto, ON M4K 2T8

Phone: 647-512-7730

Mobile: 416-273-5094

Fax: 647-512-7731

Email: selvakumar.nadarasan@mailbrook.example

www.quendrix.example
Updates

Hi everyone,

In terms of all the designs I have seen so far, here is what I like:

1.  I really like the "back" part of this design.  The "front" looks pretty decent as well, but for the "front", look at #2 on this list.  I like that.

http://www.pitchboard.example/image.aspx?imageLocation=1000_10001_2000_image.jpg&type=design300px&whiteLabelCustId=9999

2. "Side 1" of this I like, the front needs to be reworked.

http://www.pitchboard.example/image.aspx?imageLocation=1000_10002_2000_image.png&type=design300px&whiteLabelCustId=9999

3. http://www.pitchboard.example/image.aspx?imageLocation=1000_10003_2000_image.jpg&type=design300px&whiteLabelCustId=9999

4. http://www.pitchboard.example/image.aspx?imageLocation=1000_10004_2000_image.jpg&type=design300px&whiteLabelCustId=9999

Target Market(s)

We are focused on enterprise customers right now, so businesses with a long-term goal of also reaching out to the consumer market as well.

Industry/Entity Type

Software

Requirements
Must have
• Must look cool, ultra-modern, clean and eye-catching. Must incorporate our logo and the colors found in the logo.

```html
<!DOCTYPE html>
<html lang="en">
<head>
<meta charset="utf-8">
<title>Quendrix Technologies Inc. – Identity and Business Card</title>
<link rel="stylesheet" href="https://fonts.googleapis.com/css2?family=Source+Sans+3:wght@400;600&display=swap">
<style>
  :root {
    --ink: #231f20;
    --stage: #231f20;
    --paper: #ffffff;
    --card-light: #f4f5f2;
    --brand-green: #7aac43;
    --lime: #c5d634;
    --white: #ffffff;
  }
  * { box-sizing: border-box; margin: 0; padding: 0; }
  html, body { width: 941px; height: 1200px; overflow: hidden; }
  body {
    position: relative;
    background: var(--paper);
    font-family: "Source Sans 3", "Myriad Pro", Arial, sans-serif;
    color: var(--ink);
  }

  /* Identity header */
  .identity {
    position: absolute; left: 0; top: 0; width: 941px; height: 281px;
    background: var(--paper);
  }
  .identity-mark {
    position: absolute; left: 186px; top: 44px; width: 130px; height: 130px;
    border-radius: 50%; background: var(--lime);
  }
  .identity-name {
    position: absolute; left: 378px; top: 56px;
    font-size: 92px; font-weight: 400; line-height: 1; letter-spacing: 1px;
    color: var(--ink);
  }

  /* Presentation stage */
  .stage {
    position: absolute; left: 0; top: 281px; width: 941px; height: 919px;
    background: var(--stage);
  }

  /* Card back (green) */
  .card-back {
    position: absolute; left: 126px; top: 312px; width: 686px; height: 373px;
    background: var(--brand-green); overflow: hidden;
  }
  .card-back-ring {
    position: absolute; left: 96px; top: 86px; width: 250px; height: 250px;
    border-radius: 50%; border: 42px solid var(--card-light);
  }
  .card-back-name {
    position: absolute; left: 409px; top: 158px;
    font-size: 46px; font-weight: 400; line-height: 1; color: var(--white);
  }
  .card-back-url {
    position: absolute; left: 394px; top: 260px;
    font-size: 14px; letter-spacing: 4.2px; color: var(--white);
  }

  /* Card front (light) */
  .card-front {
    position: absolute; left: 126px; top: 739px; width: 686px; height: 373px;
    background: var(--card-light); overflow: hidden;
  }
  .card-front-mark {
    position: absolute; left: 34px; top: 38px; width: 80px; height: 80px;
    border-radius: 50%; background: var(--lime);
  }
  .card-front-name {
    position: absolute; left: 138px; top: 56px;
    font-size: 50px; font-weight: 400; line-height: 1; color: var(--ink);
  }
  .name-band {
    position: absolute; left: 0; top: 159px; width: 445px; height: 60px;
    background: var(--brand-green); color: var(--white);
    padding: 5px 0 0 50px; font-size: 19px; line-height: 27px;
  }
  .card-front-ring {
    position: absolute; left: 415px; top: 134px; width: 86px; height: 86px;
    border-radius: 50%; border: 14px solid var(--brand-green);
  }
  .contact-block {
    position: absolute; left: 50px; top: 280px;
    font-size: 15px; line-height: 18px; color: var(--brand-green);
  }
  .contact-block .email { margin-top: 12px; }
  .phone-list {
    position: absolute; left: 356px; top: 252px; list-style: none;
    font-size: 15px; color: var(--brand-green);
  }
  .phone-list li { display: flex; align-items: center; height: 34px; }
  .phone-list svg { width: 26px; height: 26px; margin-right: 8px; flex: none; }
</style>
</head>
<body>
  <header class="identity">
    <span class="identity-mark" aria-hidden="true"></span>
    <h1 class="identity-name">Quendrix</h1>
  </header>

  <main class="stage"></main>

  <section class="card-back" aria-label="Business card back">
    <span class="card-back-ring" aria-hidden="true"></span>
    <p class="card-back-name">Quendrix</p>
    <p class="card-back-url">www.quendrix.example</p>
  </section>

  <section class="card-front" aria-label="Business card front">
    <span class="card-front-mark" aria-hidden="true"></span>
    <p class="card-front-name">Quendrix</p>

    <div class="name-band">
      <p class="person-name">Selvakumar (Selv) Nadarasan</p>
      <p class="person-title">Founder and CEO</p>
    </div>
    <span class="card-front-ring" aria-hidden="true"></span>

    <address class="contact-block" style="font-style:normal">
      <p>47 Brindle Court, Suite 311</p>
      <p>Toronto, ON M4K 2T8</p>
      <p class="email">selvakumar.nadarasan@mailbrook.example</p>
    </address>

    <ul class="phone-list">
      <li>
        <svg viewBox="0 0 26 26" aria-label="Phone"><path d="M6 3 L10 3 L12 8 L9.5 10 Q12 15 16 17 L18 14.5 L23 16.5 L23 20.5 Q21 23 17 22 Q6 18 3 8 Q3 4 6 3 Z" fill="none" stroke="#7aac43" stroke-width="1.4"/></svg>
        <span>647-512-7730</span>
      </li>
      <li>
        <svg viewBox="0 0 26 26" aria-label="Mobile"><rect x="8" y="5" width="10" height="19" rx="2" fill="none" stroke="#7aac43" stroke-width="1.4"/><line x1="9" y1="5" x2="9" y2="1" stroke="#7aac43" stroke-width="1.4"/><rect x="10" y="8" width="6" height="5" fill="none" stroke="#7aac43" stroke-width="1"/></svg>
        <span>416-273-5094</span>
      </li>
      <li>
        <svg viewBox="0 0 26 26" aria-label="Fax"><rect x="7" y="4" width="12" height="10" fill="none" stroke="#7aac43" stroke-width="1.4"/><path d="M3 15 L23 15 L25 22 L1 22 Z" fill="none" stroke="#7aac43" stroke-width="1.4"/></svg>
        <span>647-512-7731</span>
      </li>
    </ul>
  </section>
</body>
</html>
```